Business Cards for cafe providing speciality coffee and food

I need a business card design for my husband’s businesses. He has two cafes in Brisbane. The business name is Copperleaf Roasting House. They sell high end specialty coffee as well as breakfast and lunch. All the food is cooked fresh, in house and they have strict quality controls for their coffee. I would like the business card to feature the address for both cafes, my husband’s phone number and the business’s instagram. The address for the first is 61 Wexley Crescent, Pine Hollow and the second is 23 Dorrit Avenue, Sallowmere. The Instagram handle is @copperleafroastinghouse and phone number is 0491326085. We already have a business logo that is attached.

Target Market(s)

All ages, higher disposable income and more likely to eat out regularly

Industry/Entity Type

Hospitality

Contact Information for Business Card

Must be suitable for both customers and suppliers

Font styles to use
Sans Serif

Colors

Designer to choose colors to be used in the design.

Requirements
Must have
• Owner’s name: Griff Tallant
• Addresses of both cafes: 61 Wexley Crescent, Pine Hollow and 23 Dorrit Avenue, Sallowmere
• Instagram handle: @copperleafroastinghouse
• Contact number: 0491326085
Nice to have
• Business logo

```html
<!DOCTYPE html>
<html lang="en">
<head>
<meta charset="utf-8">
<title>Copperleaf Roasting House – Business Card</title>
<link rel="stylesheet" href="https://fonts.googleapis.com/css2?family=Teko:wght@400;500;600&display=swap">
<style>
  :root {
    --backdrop: #d3e3de;
    --card: #ffffff;
    --ink: #0b0b0b;
    --paper-text: #ffffff;
  }
  * { box-sizing: border-box; margin: 0; padding: 0; }
  html, body { width: 1200px; height: 1199px; overflow: hidden; }
  body {
    background: var(--backdrop);
    font-family: "Teko", "Arial Narrow", sans-serif;
    color: var(--ink);
    position: relative;
  }
  .card {
    position: absolute;
    left: 250px;
    width: 700px;
    height: 400px;
    background: var(--card);
  }
  .card--front { top: 146px; }
  .card--back { top: 652px; }

  .brand-mark {
    position: absolute;
    left: 0; right: 0; top: 118px;
    display: flex; flex-direction: column; align-items: center;
  }
  .brand-mark__dot {
    width: 56px; height: 56px; border-radius: 50%;
    background: var(--ink);
    margin-bottom: 14px;
  }
  .brand-mark__name {
    font-weight: 500;
    font-size: 40px;
    line-height: 1;
    letter-spacing: 1px;
    text-transform: uppercase;
    text-align: center;
    color: var(--ink);
  }

  .details { position: absolute; left: 35px; top: 62px; }
  .details__name {
    font-weight: 600;
    font-size: 50px;
    line-height: 1;
    text-transform: uppercase;
  }
  .details__company {
    position: absolute; top: 162px; left: 0;
    white-space: nowrap;
    font-weight: 500; font-size: 30px; line-height: 1;
    text-transform: uppercase;
  }
  .contact-line {
    position: absolute; left: 0;
    display: flex; align-items: center;
    white-space: nowrap;
    font-weight: 400; font-size: 20px; line-height: 1;
    text-transform: uppercase;
  }
  .contact-line::before {
    content: ""; width: 2px; height: 18px; background: var(--ink);
    margin-right: 6px;
  }
  .contact-line svg { width: 14px; height: 14px; margin-right: 12px; fill: var(--ink); }
  .contact-line--phone { top: 68px; }
  .contact-line--addr1 { top: 212px; }
  .contact-line--addr2 { top: 251px; }

  .social-panel {
    position: absolute;
    left: 472px; top: 20px;
    width: 208px; height: 358px;
    background: var(--ink);
    color: var(--paper-text);
    text-align: center;
    text-transform: uppercase;
  }
  .social-panel__mark {
    position: absolute; top: 60px; left: 50%;
    width: 56px; height: 56px; margin-left: -28px;
    border-radius: 50%; background: var(--paper-text);
  }
  .social-panel__brand {
    position: absolute; top: 122px; left: 0; right: 0;
    font-size: 15px; font-weight: 500; line-height: 1;
  }
  .social-panel__follow {
    position: absolute; top: 206px; left: 0; right: 0;
    font-size: 17px; font-weight: 500; line-height: 1;
  }
  .social-panel__square {
    position: absolute; top: 232px; left: 50%;
    width: 34px; height: 34px; margin-left: -17px;
    border-radius: 7px; background: var(--paper-text);
  }
  .social-panel__handle {
    position: absolute; top: 286px; left: 0; right: 0;
    font-size: 17px; font-weight: 500; line-height: 1;
  }
</style>
</head>
<body>
  <section class="card card--front">
    <div class="brand-mark">
      <span class="brand-mark__dot"></span>
      <p class="brand-mark__name">Copperleaf<br>Roasting House</p>
    </div>
  </section>

  <section class="card card--back">
    <div class="details">
      <h1 class="details__name">Griff Tallant</h1>
      <p class="contact-line contact-line--phone">
        <svg viewBox="0 0 24 24" aria-hidden="true"><path d="M6.6 10.8a15.1 15.1 0 0 0 6.6 6.6l2.2-2.2a1 1 0 0 1 1-.25 11.4 11.4 0 0 0 3.6.57 1 1 0 0 1 1 1V20a1 1 0 0 1-1 1A17 17 0 0 1 3 4a1 1 0 0 1 1-1h3.5a1 1 0 0 1 1 1c0 1.25.2 2.45.57 3.57a1 1 0 0 1-.25 1z"/></svg>
        0491326085
      </p>
      <h2 class="details__company">Copperleaf Roasting House</h2>
      <p class="contact-line contact-line--addr1">
        <svg viewBox="0 0 24 24" aria-hidden="true"><path d="M12 2a7 7 0 0 0-7 7c0 5.25 7 13 7 13s7-7.75 7-13a7 7 0 0 0-7-7zm0 9.5A2.5 2.5 0 1 1 12 6.5a2.5 2.5 0 0 1 0 5z"/></svg>
        61 Wexley Crescent, Pine Hollow
      </p>
      <p class="contact-line contact-line--addr2">
        <svg viewBox="0 0 24 24" aria-hidden="true"><path d="M12 2a7 7 0 0 0-7 7c0 5.25 7 13 7 13s7-7.75 7-13a7 7 0 0 0-7-7zm0 9.5A2.5 2.5 0 1 1 12 6.5a2.5 2.5 0 0 1 0 5z"/></svg>
        23 Dorrit Avenue, Sallowmere
      </p>
    </div>

    <aside class="social-panel">
      <span class="social-panel__mark"></span>
      <p class="social-panel__brand">Copperleaf Roasting House</p>
      <p class="social-panel__follow">Follow us on</p>
      <span class="social-panel__square"></span>
      <p class="social-panel__handle">@copperleafroastinghouse</p>
    </aside>
  </section>
</body>
</html>
```